KDR Business Card

Keystone Draper Resources is a successful and reputable financial services company.Our main services are home loans, commercial loans, vehicle finance and equipment finance. We also do development finance for property developers. Our company is always evolving to always be an industry leader in best financial service practices with access to the largest range of lenders in the country.

We want the business card to reflect our national finance company. Modern, professional corporate image. At the same time the concept of Keystone Draper Resources is that we help build wealth for you but the process for the client is an enjoyable peaceful experience. Not stressful at all .....

Colors to be same as the logo .... gold silver black white as the options

On the reverse side of the card I wanted either just the logo symbol or the logo symbol and text of the logo ....

It could be on a black background ..... or silver or gold .... want it to be quite striking to look at when you first see the card.

On the other side of the card I wanted the following details:

Martin Haldane
Director

0438 927 604

martin@kdrgrp.com.au

Po Box 718
Ferndale ACT 2614

www.kdrgrp.com.au

ACN 618 204 957 (This can be in very small print and can be in the bottom corner of the card or somewhere not very prominent)

As requested Ive uploaded the logo file in both .ai and .pdf formats. Please let me know if you need anything else. Thanks

Reason: Still deciding on which design I like best. I will provide individual feedback as well.

```html
<!DOCTYPE html>
<html lang="en">
<head>
<meta charset="utf-8">
<title>KDR Business Card</title>
<link rel="stylesheet" href="https://fonts.googleapis.com/css2?family=Open+Sans:wght@400;700&display=swap">
<style>
  :root {
    --backdrop: #e7e6ea;
    --card: #ffffff;
    --gold: #c9a23f;
    --gold-light: #e6c970;
    --silver-flat: #e8e8ea;
    --band-grey: #8a8a8c;
    --ink: #555558;
  }
  * { margin: 0; padding: 0; box-sizing: border-box; }
  html, body { width: 1200px; height: 1000px; overflow: hidden; }
  body { background: var(--backdrop); font-family: "Open Sans", Arial, sans-serif; position: relative; }

  .card {
    position: absolute; left: 265px; width: 665px; height: 397px;
    background: var(--card); border-radius: 22px; overflow: hidden;
    box-shadow: 0 6px 18px rgba(0,0,0,0.18);
  }
  .card-front { top: 73px; }
  .card-back { top: 533px; }

  .brand { position: absolute; display: flex; align-items: center; gap: 18px; }
  .brand-dot { width: 64px; height: 64px; border-radius: 50%; background: var(--gold); flex: none; }
  .brand-name {
    font-family: "Open Sans", Arial, sans-serif; font-weight: 700; color: var(--gold);
    font-size: 28px; line-height: 1.12;
  }
  .brand-name span { display: block; }

  .card-front .brand { left: 150px; top: 157px; }

  .back-art { position: absolute; inset: 0; }
  .card-back .brand-name { position: absolute; left: 269px; top: 66px; }

  .contact { position: absolute; left: 269px; top: 173px; color: var(--ink); font-size: 15px; line-height: 1.35; }
  .contact-name { color: var(--gold); font-weight: 700; font-size: 20px; line-height: 1.1; }
  .contact-role { margin-bottom: 14px; }
  .contact-row { display: flex; align-items: center; gap: 8px; }
  .contact-row svg { width: 15px; height: 13px; fill: var(--gold); }
  .contact-address { margin-top: 12px; line-height: 1.05; }
  .contact-acn { margin-top: 12px; }

  .website { position: absolute; left: 26px; bottom: 12px; color: #ffffff; font-size: 14px; }
</style>
</head>
<body>

<section class="card card-front" aria-label="Card front">
  <div class="brand">
    <div class="brand-dot"></div>
    <div class="brand-name">
      <span>Keystone Draper</span>
      <span>Resources</span>
    </div>
  </div>
</section>

<section class="card card-back" aria-label="Card back">
  <svg class="back-art" viewBox="0 0 665 397" aria-hidden="true">
    <defs>
      <linearGradient id="goldBand" x1="0" x2="1">
        <stop offset="0" stop-color="#e6c970"/>
        <stop offset="1" stop-color="#c9a23f"/>
      </linearGradient>
    </defs>
    <path d="M0 300 C 160 365, 420 372, 665 360 L665 397 L0 397 Z" fill="#8a8a8c"/>
    <path d="M190 338 C 360 372, 520 362, 665 336 L665 358 C 520 380, 350 384, 190 345 Z" fill="url(#goldBand)"/>
    <circle cx="102" cy="185" r="150" fill="#e8e8ea"/>
  </svg>

  <div class="brand-name">
    <span>Keystone Draper</span>
    <span>Resources</span>
  </div>

  <div class="contact">
    <div class="contact-name">Martin Haldane</div>
    <div class="contact-role">Director</div>
    <div class="contact-row">
      <svg viewBox="0 0 15 11"><path d="M0 0h15v11H0z"/><path d="M1 1.2l6.5 4.8 6.5-4.8" fill="none" stroke="#fff" stroke-width="1.2"/></svg>
      <span>martin@kdrgrp.com.au</span>
    </div>
    <div class="contact-row">
      <svg viewBox="0 0 24 24"><path d="M6.6 10.8a15 15 0 0 0 6.6 6.6l2.2-2.2a1 1 0 0 1 1-.25 11.4 11.4 0 0 0 3.6.6 1 1 0 0 1 1 1V20a1 1 0 0 1-1 1A17 17 0 0 1 3 4a1 1 0 0 1 1-1h3.5a1 1 0 0 1 1 1c0 1.25.2 2.45.6 3.6a1 1 0 0 1-.25 1z"/></svg>
      <span>0438 927 604</span>
    </div>
    <div class="contact-address">Po Box 718<br>Ferndale ACT 2614</div>
    <div class="contact-acn">ACN 618 204 957</div>
  </div>

  <div class="website">www.kdrgrp.com.au</div>
</section>

</body>
</html>
```